Ridgeline Orchards Rainier POS Card 7"H x 11"W

We are wanting to create a one-sided 7 x 11 Rainier cherry card that is eye catching and informative.This should be clear and easy to read and not cluttered. We use these cards as a display in grocery stores, demo stands, and other events to market Northwest Rainier Cherries. We have a few facts that we would like displayed on the card (see below).

Target Market(s)

Consumers

Industry/Entity Type

Agriculture

Font styles to use
Sans Serif

Requirements
Must have
• Yellow cherries - yellow fruit (the blush on the skin is a kiss from the sun)
• Juice doesn't stain - Kid Friendly
• Add contrast to your summer table
• Sweetest Variety - still low glycemic
• Source of Vitamin C, Source of Potassium, and Source of Melatonin
• Rainiers take up to 4x as much work as red cherries
• Natural Color palettes
• Easy to read
• Ridgeline Orchards
Nice to have
• Unique, creative, realistc Rainier cherry designs
Should not have
• pastel or neon color scheme, overly cutesy elements

```html
<!DOCTYPE html>
<html lang="en">
<head>
<meta charset="utf-8">
<title>Ridgeline Orchards – Yellow Cherries Card</title>
<link rel="stylesheet" href="https://fonts.googleapis.com/css2?family=Great+Vibes&family=Open+Sans:ital,wght@0,400;0,600;0,700;1,600&display=swap">
<style>
  :root {
    --kraft: #c49a6c;
    --card-black: #0d0d0d;
    --charcoal: #2a2a2a;
    --band: rgba(70, 70, 70, 0.55);
    --lemon: #fff200;
    --gold: #f7d117;
    --white: #ffffff;
    --leaf-green: #2f8a3a;
    --ring-green: #8cc04b;
    --mint: #d9eedd;
    --ink: #1a1a1a;
    --cherry-red: #7a1028;
  }
  * { margin: 0; padding: 0; box-sizing: border-box; }
  html, body {
    width: 1200px; height: 782px; overflow: hidden;
    background: var(--kraft);
    font-family: "Open Sans", Arial, sans-serif;
  }
  .card {
    position: absolute; left: 25px; top: 28px;
    width: 1154px; height: 728px; overflow: hidden;
    background:
      radial-gradient(ellipse 420px 300px at 1040px 60px, #4a4a4a 0%, rgba(40,40,40,0) 70%),
      var(--card-black);
  }
  .title {
    position: absolute; left: 44px; top: 18px;
    font-family: "Great Vibes", cursive;
    font-size: 118px; line-height: 1; color: var(--lemon);
    white-space: nowrap;
  }
  .fact-band {
    position: absolute; left: 0; width: 1154px; height: 58px;
    background: linear-gradient(90deg, var(--band), rgba(90,90,90,0.5));
    display: flex; align-items: center; padding-left: 49px;
    color: var(--white); white-space: nowrap;
  }
  .fact-band strong { font-weight: 700; font-size: 37px; }
  .fact-band span { font-weight: 400; font-size: 27px; margin-left: 12px; }
  .band-sweet { top: 224px; }
  .band-stain { top: 290px; }
  .band-table { top: 356px; }
  .effort-note {
    position: absolute; left: 47px; top: 430px;
    font-size: 30px; font-weight: 600; color: var(--lemon);
    white-space: nowrap;
  }
  .fruit-photo {
    position: absolute; left: 636px; top: 44px;
    width: 520px; height: 436px; border-radius: 48% 52% 46% 54%;
    background: radial-gradient(circle at 45% 55%, #ffd21a 0%, #f6b414 55%, rgba(230,150,20,0) 75%);
  }
  .swoosh { position: absolute; left: 0; top: 0; }
  .nutrition-badge {
    position: absolute; left: 528px; top: 500px;
    width: 208px; height: 208px; border-radius: 50%;
    background: var(--ring-green);
    display: flex; align-items: center; justify-content: center;
  }
  .nutrition-badge p {
    width: 182px; height: 182px; border-radius: 50%;
    background: radial-gradient(circle at 45% 40%, #ffffff 60%, #e6e6e6 100%);
    display: flex; align-items: center; justify-content: center; text-align: center;
    font-style: italic; font-weight: 600; font-size: 19px; line-height: 26px;
    color: var(--leaf-green);
  }
  .fruit-note {
    position: absolute; right: 56px; top: 494px; text-align: right;
    color: var(--white); font-size: 25px; line-height: 38px;
  }
  .fruit-note .lead { font-size: 30px; }
  .brand {
    position: absolute; left: 76px; top: 620px;
    display: flex; align-items: center; gap: 18px;
  }
  .brand-dot { width: 58px; height: 58px; border-radius: 50%; background: var(--cherry-red); }
  .brand-name { font-size: 42px; font-weight: 600; color: var(--ink); white-space: nowrap; }
</style>
</head>
<body>
<main class="card">
  <h1 class="title">Yellow Cherries</h1>

  <div class="fruit-photo" role="img" aria-label="Photo of three ripe yellow Rainier cherries with green leaves"></div>

  <p class="fact-band band-sweet"><strong>Sweetest Variety</strong><span>- Still low glycemic</span></p>
  <p class="fact-band band-stain"><strong>Juice doesn't stain</strong><span>- Kid Friendly</span></p>
  <p class="fact-band band-table"><strong>Add contrast to your summer table</strong></p>

  <p class="effort-note">Rainiers take up to 4x as much work as red cherries</p>

  <svg class="swoosh" width="1154" height="728" viewBox="0 0 1154 728" aria-hidden="true">
    <path fill="var(--gold)" d="M0,545 C220,470 480,495 700,580 S1000,690 1154,645 L1154,700 C1000,728 850,700 700,648 S260,525 0,585 Z"/>
    <path fill="var(--white)" d="M0,575 C250,520 500,565 700,638 S1000,722 1154,700 L1154,728 L0,728 Z"/>
    <path fill="none" stroke="var(--leaf-green)" stroke-width="3" d="M0,575 C250,520 500,565 700,638 S1000,722 1154,700"/>
    <path fill="none" stroke="var(--mint)" stroke-width="8" d="M0,588 C250,533 500,578 700,651 S1000,735 1154,713"/>
  </svg>

  <div class="nutrition-badge">
    <p>Source of<br>Vitamin C, Source<br>of Potassium, and<br>Source of<br>Melatonin</p>
  </div>

  <p class="fruit-note"><span class="lead">Yellow Fruit</span><br>(the blush on the skin<br>is a kiss from the sun)</p>

  <div class="brand">
    <span class="brand-dot"></span>
    <span class="brand-name">Ridgeline Orchards</span>
  </div>
</main>
</body>
</html>
```